Website for sailing around the world

I'm planning to sail around the world with a sailing katamaran in about 8 jears. Together with my best friend we want to be "on tour" for at least 10 jears (or more). I have no idea about webdesign. It should be a wordpress site. I would like to have some links like: "about us", "about the boat", if possible i woul like to show: where is the boat rigt now, links to facebook, twitter, google+ ect., an archive to list all our daily- weekly blog articles which we will send from the boat to the website...
I already tried to build a wordpress website, but its not good enough 😩.
The boat name is: VorraBay
Maby you want to see the website i try to build by myself: vorrabay.example-blogs.net

Until i am collecting money for this trip i want to "play" with this website during my sailing-holidays (getting better in uploading block-articles, getting better in "using" my webste).

Target Market(s)

Webdesign
Sailing Blog

Industry/Entity Type

Tour

Colors

Designer to choose colors to be used in the design.

Requirements
Must have
• Should be nice to view.
• Must be easy to handle for "non it person" (me)
• Liks to facebook, twitter, google+
• People who follow us on wordpress should be informed if we post a new blog article...
Nice to have
• Please see my first adventure on wordpress:
• Vorrabay.example-blogs.net
• (Here i tried to build a website by my own, but i am not good in this...
• Maby someone can build an account on fb,twitter, google+ (something with "vorraBay" in the account-name...

```html
<!DOCTYPE html>
<html lang="en">
<head>
<meta charset="utf-8">
<title>VorraBay – Sailing around the world</title>
<link rel="stylesheet" href="https://fonts.googleapis.com/css2?family=Poppins:wght@400;500;600;700&family=Open+Sans:wght@400;600&display=swap">
<style>
:root{
  --ink:#222;
  --muted:#8a8a8a;
  --line:#e4e4e4;
  --white:#fff;
  --panel:#3b3e43;
  --footer:#efefef;
  --sea-a:#8fb3c9;
  --sea-b:#4d6c80;
}
*{box-sizing:border-box;margin:0;padding:0}
html,body{width:1200px;height:2912px;overflow:hidden;background:var(--white)}
body{font-family:"Open Sans",Arial,sans-serif;color:var(--ink);position:relative}
h1,h2,h3,h4,.logo,.nav a,.btn{font-family:"Poppins",Arial,sans-serif}

.hero{position:absolute;left:0;top:0;width:1200px;height:720px;overflow:hidden}
.hero-photo{position:absolute;inset:0;background:linear-gradient(160deg,#dfe7ec 0%,#c4d0d8 40%,#8f9ea8 75%,#5d6a72 100%)}
.hero-shade{position:absolute;inset:0;background:rgba(20,25,30,.28)}
.topbar{position:absolute;left:0;top:0;width:1200px;height:96px;background:rgba(30,30,30,.55);display:flex;align-items:center;justify-content:space-between;padding:0 80px 0 112px}
.logo{color:var(--white);font-weight:600;font-size:34px;letter-spacing:.5px}
.nav{display:flex;gap:44px}
.nav a{color:var(--white);text-decoration:none;font-size:17px;font-weight:500}
.hero-copy{position:absolute;left:0;top:350px;width:1200px;text-align:center;color:var(--white)}
.hero-copy h1{font-size:38px;font-weight:700;line-height:50px;text-shadow:0 2px 8px rgba(0,0,0,.3)}
.btn{display:inline-block;border:2px solid var(--white);color:var(--white);font-size:15px;font-weight:500;letter-spacing:1px;text-transform:uppercase;padding:14px 30px}
.hero-copy .btn{margin-top:40px}

.boat{position:absolute;left:108px;top:760px;width:976px;height:408px;display:flex}
.boat-photo{width:632px;height:408px;background:linear-gradient(180deg,#7fc3e0 0%,#bfe3ef 45%,#2fa7bf 60%,#137b92 100%)}
.boat-info{flex:1;background:var(--panel);color:var(--white);padding:44px 32px}
.boat-info h2{font-size:22px;font-weight:600}
.boat-info .loc{font-size:14px;font-weight:600;margin-top:30px}
.boat-info p{font-size:13px;line-height:22px;color:#cfd2d6;margin-top:20px}
.boat-info .btn{margin-top:40px;font-size:13px;padding:12px 22px}

.section-title{font-size:22px;font-weight:600}
.blog-head{position:absolute;left:108px;top:1264px;width:644px;display:flex;justify-content:space-between;align-items:center}
.arrows{display:flex;gap:14px}
.post{position:absolute;width:312px}
.post-photo{width:312px;height:240px}
.post h3{font-size:17px;font-weight:600;margin-top:26px;line-height:24px}
.post .meta{font-size:12px;color:var(--muted);margin-top:4px}
.post p{font-size:13px;line-height:22px;color:var(--muted);margin-top:16px}

.sidebar{position:absolute;left:772px;top:1252px;width:312px}
.search{height:60px;border:1px solid var(--line);display:flex;align-items:center;justify-content:space-between;padding:0 18px;font-size:15px}
.widget-title{font-size:20px;font-weight:600;margin-top:48px;padding-bottom:14px;border-bottom:2px solid var(--ink);display:inline-block}
.recent{position:relative;height:240px;margin-top:26px}
.recent .shot{position:absolute;inset:0}
.recent h4{position:absolute;left:20px;bottom:22px;color:var(--white);font-size:16px;font-weight:600}
.list{list-style:none;margin-top:22px}
.list li{font-size:15px;padding:12px 0;border-bottom:1px solid var(--line)}

.footer{position:absolute;left:0;top:2752px;width:1200px;height:160px;background:var(--footer);text-align:center;padding-top:30px}
.footer .logo{color:var(--ink);font-size:30px}
.social{display:flex;justify-content:center;gap:18px;margin-top:14px}
.social span{width:22px;height:22px;border-radius:50%;background:#555;display:block}
.copy{font-size:12px;color:#555;margin-top:16px}
</style>
</head>
<body>

<header class="hero">
  <div class="hero-photo" role="img" aria-label="Sailor at the helm of a catamaran under an overcast sky"></div>
  <div class="hero-shade"></div>
  <div class="topbar">
    <div class="logo">vorrabay</div>
    <nav class="nav">
      <a href="#">Home</a><a href="#">About Us</a><a href="#">About The Boat</a><a href="#">Contact Us</a>
    </nav>
  </div>
  <div class="hero-copy">
    <h1>Catamaran VorraBay on world<br>circum navigation!</h1>
    <a class="btn" href="#">Make a tour</a>
  </div>
</header>

<section class="boat">
  <div class="boat-photo" role="img" aria-label="White catamaran anchored in turquoise water"></div>
  <div class="boat-info">
    <h2>My Boat Now In</h2>
    <div class="loc">Location : Fjords, Norway</div>
    <p>We have been sailing along the quiet fjords for days now, anchoring in calm bays between steep green cliffs and small fishing villages, waiting for good winds.</p>
    <a class="btn" href="#">Find my location</a>
  </div>
</section>

<div class="blog-head">
  <h2 class="section-title">Featured Blog Posts</h2>
  <div class="arrows">
    <svg width="10" height="14" viewBox="0 0 10 14"><path d="M8 1 2 7l6 6" fill="none" stroke="#999" stroke-width="2"/></svg>
    <svg width="10" height="14" viewBox="0 0 10 14"><path d="M2 1l6 6-6 6" fill="none" stroke="#222" stroke-width="2"/></svg>
  </div>
</div>

<article class="post" style="left:108px;top:1360px">
  <div class="post-photo" role="img" aria-label="Sailor steering a yacht on open sea" style="background:linear-gradient(180deg,#c9dbe6,#8aa6b8)"></div>
  <h3>Große Routenplanung</h3>
  <div class="meta">2 Juni 2014 / Hinterlasse einen Kommentar</div>
  <p>Wir haben die ganze Woche Seekarten studiert und die ersten Etappen unserer großen Reise sorgfältig geplant.</p>
</article>
<article class="post" style="left:440px;top:1360px">
  <div class="post-photo" role="img" aria-label="Limestone islands rising from a calm bay" style="background:linear-gradient(180deg,#d9d3c4,#7a8c7a)"></div>
  <h3>Einkaufsliste</h3>
  <div class="meta">2 Juni 2014 / Hinterlasse einen Kommentar</div>
  <p>Was wir für lange Tage auf See brauchen: Vorräte, Wasser, Ersatzteile und genug Kaffee für die Nachtwachen.</p>
</article>
<article class="post" style="left:108px;top:1828px">
  <div class="post-photo" role="img" aria-label="Junk boat with red sails at sunset" style="background:linear-gradient(180deg,#f1c27d,#b5523a)"></div>
  <h3>Natus error sit voluptatem accusa</h3>
  <div class="meta">2 Juni 2014 / Hinterlasse einen Kommentar</div>
  <p>Ein ruhiger Abend im Hafen, die Sonne geht unter und wir schreiben die ersten Zeilen in unser Logbuch.</p>
</article>
<article class="post" style="left:440px;top:1828px">
  <div class="post-photo" role="img" aria-label="Skipper in a white cap at the wheel of a sailboat" style="background:linear-gradient(180deg,#cfe4f0,#5f8fb0)"></div>
  <h3>Accusamus et iusto odio</h3>
  <div class="meta">2 Juni 2014 / Hinterlasse einen Kommentar</div>
  <p>Frischer Wind aus Nordwest, volle Segel und zwei zufriedene Freunde an Bord auf dem Weg zur nächsten Insel.</p>
</article>
<article class="post" style="left:108px;top:2292px">
  <div class="post-photo" role="img" aria-label="Traveller looking over a tropical bay with islands" style="background:linear-gradient(180deg,#9cc6d6,#3d6a58)"></div>
  <h3>Similique sunt in culpa qui officia</h3>
  <div class="meta">2 Juni 2014 / Hinterlasse einen Kommentar</div>
  <p>Vom Aussichtspunkt sehen wir unsere Ankerbucht und freuen uns schon auf den nächsten Schlag übers Meer.</p>
</article>
<article class="post" style="left:440px;top:2292px">
  <div class="post-photo" role="img" aria-label="Boats on a river at golden hour" style="background:linear-gradient(180deg,#e8b07a,#7d4c32)"></div>
  <h3>Nam libero tempore, cum</h3>
  <div class="meta">2 Juni 2014 / Hinterlasse einen Kommentar</div>
  <p>Ein Tag auf dem Fluss, goldenes Licht auf dem Wasser und viele neue Eindrücke für unseren nächsten Bericht.</p>
</article>

<aside class="sidebar">
  <div class="search">
    <span>Search</span>
    <svg width="16" height="16" viewBox="0 0 16 16"><circle cx="6.5" cy="6.5" r="5" fill="none" stroke="#222" stroke-width="2"/><path d="M10.5 10.5 15 15" stroke="#222" stroke-width="2"/></svg>
  </div>
  <h3 class="widget-title">Recent Articles</h3>
  <div class="recent">
    <div class="shot" role="img" aria-label="Travellers on a harbour pier" style="background:linear-gradient(180deg,#8fb1c4,#3e5666)"></div>
    <h4>Sed ut perspiciatis</h4>
  </div>
  <div class="recent">
    <div class="shot" role="img" aria-label="Fishing boats in a harbour at sunset" style="background:linear-gradient(180deg,#e0a36a,#5a3a2a)"></div>
    <h4>Maxime placeat facere possimus</h4>
  </div>
  <h3 class="widget-title">Categories</h3>
  <ul class="list"><li>Allgemein</li></ul>
  <h3 class="widget-title">Archive</h3>
  <ul class="list"><li>2014</li></ul>
  <h3 class="widget-title">Meta</h3>
  <ul class="list">
    <li>Registrieren</li><li>Anmelden</li><li>Beiträge-Feed (RSS)</li><li>Kommentare als RSS</li>
  </ul>
</aside>

<footer class="footer">
  <div class="logo">vorrabay</div>
  <div class="social"><span></span><span></span><span></span></div>
  <div class="copy">© 2017 VorraBay. | All Rights Reserved</div>
</footer>

</body>
</html>
```